Business card design needed

Looking for an innovative design that portrays a professional image for our company. We are a structural steel erection, EWP and crane hire company. We are looking at having business and contact details on front of card and perhaps a list of what we hire on the back of the card. Our company machine colours are royal blue and silver at present but would be open to change with our cards...
Updates
We are looking for double sided designs due to the amount of information required on the card
The Logo uploaded if the logo we have been using, however our company name has changed to just "Steady Summit Lifting". I have uploaded the image just for ideas...
Reason: Allowing more time for more design submissions
Reason: Want more dedigns
Target Market(s)
Construction/Industrial
Industry/Entity Type
Structural Steel
Contact Information for Business Card
Business Name: Steady Summit Lifting
Specialising in Structural Steel Erection, Equipment & Crane Hire
Address: 27 Corwin Street, Balmoral Q 4571
Site Contact: Dale Morven - 0431 597 203 - dale@sslifting.example
Office Contact: Lina Fairbrook - 0419 735 214 - lina@sslifting.example
We hire Forklifts, Telehandlers, Scissor-lifts, Boom-lifts, 3T Mini Cranes, 16T/20T Bexlo, Prime mover with extendable trailer (13.5-22m), Qualified Boilermakers,Riggers and Dogman.
Logo Text
Steady Summit Lifting or SSL
Logo styles of interest
Emblem Logo
Look and feel

```html
<!DOCTYPE html>
<html lang="en">
<head>
<meta charset="utf-8">
<title>Steady Summit Lifting – Business Cards</title>
<link href="https://fonts.googleapis.com/css2?family=Pathway+Gothic+One&display=swap" rel="stylesheet">
<style>
  :root {
    --page: #ffffff;
    --ink: #0b0b0b;
    --white: #ffffff;
    --royal: #2d3fd6;
    --silver-light: #d9dfe1;
    --silver-mid: #aeb5b8;
    --silver-dark: #8d9497;
    --font: "Pathway Gothic One", "Arial Narrow", sans-serif;
  }
  html, body {
    margin: 0;
    padding: 0;
    width: 1200px;
    height: 1000px;
    overflow: hidden;
    background: var(--page);
    font-family: var(--font);
  }
  .canvas { position: relative; width: 1200px; height: 1000px; }

  .card {
    position: absolute;
    width: 600px;
    height: 369px;
    overflow: hidden;
  }
  .card--site { left: 78px; top: 84px; }
  .card--office { left: 444px; top: 605px; transform: rotate(-19.6deg); transform-origin: 0 0; }

  .card__texture {
    position: absolute; inset: 0;
    background:
      radial-gradient(ellipse at 85% 15%, var(--silver-light) 0%, transparent 55%),
      radial-gradient(ellipse at 60% 85%, var(--silver-light) 0%, transparent 50%),
      linear-gradient(135deg, var(--silver-mid) 0%, var(--silver-light) 45%, var(--silver-dark) 100%);
  }
  .card__panel { position: absolute; inset: 0; }

  .person { position: absolute; left: 45px; top: 60px; }
  .person__name {
    margin: 0; color: var(--white);
    font-size: 38px; font-weight: 400; line-height: 1;
  }
  .person__role {
    margin: 4px 0 0; color: var(--royal);
    font-size: 21px; line-height: 1;
  }

  .contacts {
    position: absolute; left: 47px; top: 210px;
    margin: 0; padding: 0; list-style: none;
  }
  .contacts li {
    display: flex; align-items: center;
    height: 27.5px;
    color: var(--white); font-size: 17px;
  }
  .contacts svg { width: 18px; height: 18px; margin-right: 17px; fill: var(--white); flex: none; }

  .brand {
    position: absolute; left: 280px; width: 320px; top: 118px;
    text-align: center;
  }
  .brand__name {
    display: inline-flex; align-items: center; gap: 8px;
    margin: 0; color: var(--ink);
    font-size: 27px; font-weight: 400; line-height: 1;
  }
  .brand__mark { width: 14px; height: 14px; background: var(--ink); }
  .brand__tagline {
    margin: 14px 0 0; color: var(--royal);
    font-size: 16px; line-height: 18px;
  }
  .hire {
    position: absolute; left: 300px; width: 300px; top: 220px;
    text-align: center; color: var(--ink);
    font-size: 13px; line-height: 21px;
  }
  .hire p { margin: 0; }
</style>
</head>
<body>
<main class="canvas">

  <!-- Site contact card -->
  <article class="card card--site">
    <div class="card__texture" role="img" aria-label="Brushed silver metal texture background"></div>
    <svg class="card__panel" viewBox="0 0 600 369" width="600" height="369" aria-hidden="true">
      <path d="M0,0 H250 C278,30 226,110 230,155 C236,225 318,300 350,369 H0 Z" fill="var(--ink)"/>
    </svg>

    <div class="person">
      <h2 class="person__name">Dale Morven</h2>
      <p class="person__role">Operations Manager</p>
    </div>

    <ul class="contacts">
      <li><svg viewBox="0 0 24 24"><path d="M6.6 2.5l3 3.6-2 2.2c1.3 3 3.7 5.4 6.6 6.7l2.2-2 3.6 3-2.2 3.2C10.5 19 5 13.5 3.6 4.8z"/></svg>0431 597 203</li>
      <li><svg viewBox="0 0 24 24"><path d="M2 5h20v2l-10 6L2 7z M2 9l10 6 10-6v10H2z"/></svg>dale@sslifting.example</li>
      <li><svg viewBox="0 0 24 24"><path d="M10 14a5 5 0 0 1 0-7l3-3a5 5 0 0 1 7 7l-2 2-1.5-1.5 2-2a3 3 0 0 0-4-4l-3 3a3 3 0 0 0 0 4z M14 10a5 5 0 0 1 0 7l-3 3a5 5 0 0 1-7-7l2-2 1.5 1.5-2 2a3 3 0 0 0 4 4l3-3a3 3 0 0 0 0-4z"/></svg>www.sslifting.example</li>
      <li><svg viewBox="0 0 24 24"><path d="M12 2a7 7 0 0 1 7 7c0 5-7 13-7 13S5 14 5 9a7 7 0 0 1 7-7zm0 4a3 3 0 1 0 0 6 3 3 0 0 0 0-6z"/></svg>27 Corwin Street, Balmoral Q 4571</li>
    </ul>

    <div class="brand">
      <p class="brand__name"><span class="brand__mark"></span>Steady Summit Lifting</p>
      <p class="brand__tagline">Specialising in Structural Steel Erection,<br>Equipment &amp; Crane Hire</p>
    </div>

    <div class="hire">
      <p>We hire:</p>
      <p>Forklifts, Telehandlers, Scissor-lifts, Boom-lifts, 3T Mini Cranes,</p>
      <p>16T/20T Bexlo, Prime mover with extendable trailer (13.5-22m),</p>
      <p>Qualified Boilermakers,Riggers and Dogman.</p>
    </div>
  </article>

  <!-- Office contact card -->
  <article class="card card--office">
    <div class="card__texture" role="img" aria-label="Brushed silver metal texture background"></div>
    <svg class="card__panel" viewBox="0 0 600 369" width="600" height="369" aria-hidden="true">
      <path d="M0,0 H250 C278,30 226,110 230,155 C236,225 318,300 350,369 H0 Z" fill="var(--ink)"/>
    </svg>

    <div class="person">
      <h2 class="person__name">Lina Fairbrook</h2>
      <p class="person__role">Office Manager</p>
    </div>

    <ul class="contacts">
      <li><svg viewBox="0 0 24 24"><path d="M6.6 2.5l3 3.6-2 2.2c1.3 3 3.7 5.4 6.6 6.7l2.2-2 3.6 3-2.2 3.2C10.5 19 5 13.5 3.6 4.8z"/></svg>0419 735 214</li>
      <li><svg viewBox="0 0 24 24"><path d="M2 5h20v2l-10 6L2 7z M2 9l10 6 10-6v10H2z"/></svg>lina@sslifting.example</li>
      <li><svg viewBox="0 0 24 24"><path d="M10 14a5 5 0 0 1 0-7l3-3a5 5 0 0 1 7 7l-2 2-1.5-1.5 2-2a3 3 0 0 0-4-4l-3 3a3 3 0 0 0 0 4z M14 10a5 5 0 0 1 0 7l-3 3a5 5 0 0 1-7-7l2-2 1.5 1.5-2 2a3 3 0 0 0 4 4l3-3a3 3 0 0 0 0-4z"/></svg>www.sslifting.example</li>
      <li><svg viewBox="0 0 24 24"><path d="M12 2a7 7 0 0 1 7 7c0 5-7 13-7 13S5 14 5 9a7 7 0 0 1 7-7zm0 4a3 3 0 1 0 0 6 3 3 0 0 0 0-6z"/></svg>27 Corwin Street, Balmoral Q 4571</li>
    </ul>

    <div class="brand">
      <p class="brand__name"><span class="brand__mark"></span>Steady Summit Lifting</p>
      <p class="brand__tagline">Specialising in Structural Steel Erection,<br>Equipment &amp; Crane Hire</p>
    </div>

    <div class="hire">
      <p>We hire:</p>
      <p>Forklifts, Telehandlers, Scissor-lifts, Boom-lifts, 3T Mini Cranes,</p>
      <p>16T/20T Bexlo, Prime mover with extendable trailer (13.5-22m),</p>
      <p>Qualified Boilermakers,Riggers and Dogman.</p>
    </div>
  </article>

</main>
</body>
</html>
```